Brightwell Systems - Company Overview Brochure

We would like a single page A4 Brochure to give to new potential customers to provide a quick overview of our company. This will be used in presales meetings.

We have included the content we would like on the brochure under "Brightwell Systems Marketing Brochure.docx".

We have included two other designs "timebundleterms v4.pdf and Brightwell Public Cloud Plans.pdf" which shows similar marketing brochures we have. We would like these designs to have the same Brightwell Blue and "Specialised Technology Consultancy firm" theme.

Target Market(s)

Technology Sector

Industry/Entity Type

Information Technology

Colors
0054AA
0677BA
7BADD7
CADEEF
E8F1F8

Requirements
Must have
• "Innovative Tech Company Theme".

```html
<!DOCTYPE html>
<html lang="en">
<head>
<meta charset="utf-8">
<title>Brightwell Systems – Specialised Consulting</title>
<link rel="stylesheet" href="https://fonts.googleapis.com/css2?family=Bebas+Neue&family=Montserrat:ital,wght@0,300;0,500;0,600;0,700;0,800;1,700&display=swap">
<style>
  :root {
    --stage: #4b4b4b;
    --paper: #ffffff;
    --navy: #1b2463;
    --navy-mid: #1f3590;
    --brand-blue: #0054aa;
    --brand-bright: #0677ba;
    --brand-light: #7badd7;
    --brand-pale: #cadeef;
    --brand-mist: #e8f1f8;
    --grey-stripe: #a9abaf;
    --link: #1f3fa8;
    --text-light: #ffffff;
  }
  * { box-sizing: border-box; margin: 0; padding: 0; }
  html, body { width: 727px; height: 1200px; overflow: hidden; }
  body { background: var(--stage); font-family: "Montserrat", sans-serif; position: relative; }

  .brochure {
    position: absolute; left: 17px; top: 114px;
    width: 692px; height: 971px;
    background: var(--paper); overflow: hidden;
    box-shadow: 0 4px 14px rgba(0,0,0,.35);
  }
  .abs { position: absolute; }

  /* header */
  .header-band { left: 0; top: 0; width: 692px; height: 137px; }
  .brand-name {
    left: 36px; top: 58px; width: 150px;
    font-weight: 700; font-size: 17px; line-height: 1.15;
    color: var(--navy-mid); display: flex; align-items: center; gap: 8px;
  }
  .brand-mark { width: 12px; height: 12px; background: var(--brand-blue); flex: none; }
  .title-light { left: 196px; top: 12px; font-weight: 300; font-size: 50px; letter-spacing: 1px; color: var(--text-light); line-height: 1; }
  .title-bold { left: 228px; top: 64px; font-weight: 800; font-size: 57px; letter-spacing: .5px; color: var(--text-light); line-height: 1; }

  /* body */
  .panel {
    left: 0; top: 145px; width: 692px; height: 773px;
    background:
      radial-gradient(circle at 80% 45%, rgba(123,173,215,.45), transparent 40%),
      radial-gradient(circle at 55% 75%, rgba(6,119,186,.45), transparent 45%),
      linear-gradient(100deg, var(--navy) 0%, var(--navy-mid) 45%, var(--brand-blue) 100%);
  }
  .stripes { left: 0; top: 145px; }
  .intro { left: 36px; top: 158px; width: 630px; font-weight: 500; font-size: 13.2px; line-height: 17px; color: var(--text-light); }

  .section-title { font-family: "Bebas Neue", sans-serif; color: var(--text-light); line-height: 1; }
  .it-title { left: 36px; top: 205px; font-size: 36px; }
  .es-title { left: 36px; top: 440px; font-size: 36px; }
  .rule { height: 2px; background: var(--text-light); }
  .divider { width: 2px; background: rgba(255,255,255,.35); top: 245px; height: 120px; }

  .service-icon { width: 112px; height: 112px; border-radius: 50%; background: var(--paper); top: 249px; }
  .service-icon span { position: absolute; inset: 24px; border-radius: 50%; background: radial-gradient(circle, var(--brand-pale), var(--brand-mist)); }
  .service-label { top: 366px; width: 160px; text-align: center; font-weight: 500; font-size: 15.5px; line-height: 16px; color: var(--text-light); }

  .mini-icon { width: 42px; height: 42px; border-radius: 50%; background: var(--paper); }
  .mini-label { font-weight: 500; font-size: 15.5px; line-height: 18px; color: var(--text-light); }

  .sub-title { left: 36px; font-size: 29px; }
  .copy { left: 36px; width: 545px; font-size: 9.6px; line-height: 14.6px; font-weight: 500; color: var(--text-light); }
  .copy-head { left: 36px; font-size: 11.5px; font-weight: 600; color: var(--text-light); }

  .footer { left: 0; top: 926px; width: 692px; text-align: center; font-weight: 700; font-style: italic; font-size: 11px; line-height: 14px; color: var(--navy); }
  .footer a { color: var(--link); text-decoration: none; }
</style>
</head>
<body>
<main class="brochure">
  <svg class="abs header-band" viewBox="0 0 692 137" aria-hidden="true">
    <defs>
      <linearGradient id="header-fill" x1="0" x2="1">
        <stop offset="0" stop-color="#0f4aa6"/>
        <stop offset="1" stop-color="#0a7ac4"/>
      </linearGradient>
    </defs>
    <polygon points="134,0 692,0 692,136 212,136" fill="url(#header-fill)"/>
  </svg>

  <div class="abs brand-name"><span class="brand-mark"></span><span>Brightwell Systems</span></div>
  <h1 class="abs title-light">SPECIALISED</h1>
  <div class="abs title-bold">CONSULTING</div>

  <div class="abs panel" role="img" aria-label="Deep blue background with a soft glowing technology network pattern"></div>

  <svg class="abs stripes" width="692" height="773" viewBox="0 0 692 773" aria-hidden="true">
    <defs>
      <linearGradient id="stripe-blue" x1="0" y1="1" x2="1" y2="0">
        <stop offset="0" stop-color="#1b2a8c"/>
        <stop offset="1" stop-color="#0a6ccd"/>
      </linearGradient>
    </defs>
    <polygon points="692,395 692,773 495,773" fill="#ffffff"/>
    <polygon points="692,420 692,470 550,773 508,773" fill="url(#stripe-blue)"/>
    <polygon points="692,670 692,700 645,773 618,773" fill="var(--grey-stripe)"/>
    <polygon points="692,720 692,773 660,773" fill="#d4d6da"/>
  </svg>

  <p class="abs intro">Brightwell Systems is a Technology Consulting Company based in Perth, Western Australia, which offers customers tailored technical solutions for a range of products.</p>

  <h2 class="abs section-title it-title">IT Services</h2>
  <div class="abs rule" style="left:172px; top:224px; width:480px;"></div>

  <div class="abs service-icon" style="left:42px;" role="img" aria-label="Project integration icon"><span></span></div>
  <div class="abs divider" style="left:176px;"></div>
  <div class="abs service-icon" style="left:196px;" role="img" aria-label="Managed services icon"><span></span></div>
  <div class="abs divider" style="left:335px;"></div>
  <div class="abs service-icon" style="left:361px;" role="img" aria-label="Enterprise security icon"><span></span></div>
  <div class="abs divider" style="left:497px;"></div>
  <div class="abs service-icon" style="left:523px;" role="img" aria-label="Software development icon"><span></span></div>

  <div class="abs service-label" style="left:18px;">Project<br>Integration</div>
  <div class="abs service-label" style="left:172px;">Managed<br>Services</div>
  <div class="abs service-label" style="left:337px;">Enterprise<br>Security</div>
  <div class="abs service-label" style="left:499px;">Software<br>Development</div>

  <h2 class="abs section-title es-title">Electronic Security &amp; Communications</h2>
  <div class="abs rule" style="left:490px; top:457px; width:100px;"></div>

  <div class="abs mini-icon" style="left:36px; top:480px;" role="img" aria-label="CCTV camera icon"></div>
  <div class="abs mini-label" style="left:88px; top:490px;">CCTV</div>
  <div class="abs mini-icon" style="left:36px; top:530px;" role="img" aria-label="Integrated security icon"></div>
  <div class="abs mini-label" style="left:88px; top:540px;">Integrated Electronic Security</div>

  <div class="abs mini-icon" style="left:384px; top:490px;" role="img" aria-label="Fibre optics icon"></div>
  <div class="abs mini-label" style="left:436px; top:490px;">Structured Cabling and<br>Fibre Optics</div>
  <svg class="abs mini-icon" style="left:384px; top:540px;" viewBox="0 0 42 42" role="img" aria-label="Wireless signal icon">
    <circle cx="21" cy="21" r="21" fill="#fff"/>
    <circle cx="21" cy="21" r="2.6" fill="#1b2463"/>
    <g fill="none" stroke="#1b2463" stroke-width="2.2" stroke-linecap="round">
      <path d="M15.5 15.5a8 8 0 0 0 0 11M26.5 15.5a8 8 0 0 1 0 11"/>
      <path d="M11.5 12a13 13 0 0 0 0 18M30.5 12a13 13 0 0 1 0 18"/>
    </g>
  </svg>
  <div class="abs mini-label" style="left:436px; top:552px;">Wireless Communications</div>

  <h2 class="abs section-title sub-title" style="top:615px;">Our Commitment</h2>
  <p class="abs copy" style="top:647px;">Our commitment to you is to do things right the first time while being fair but cost-effective. If you're looking for the cheapest consultants, Brightwell may not be the right fit for you. We are a specialised consultancy firm that offers tailored solutions to government and the enterprise sector with some of Perth's best consultants. In areas such as cybersecurity and business continuity, it pays to get it done correctly the first time in alignment with vendor best practices. There are many ways of doing things in the technology field, and only after understanding all methods of achieving an outcome can you recommend the best solution in alignment with best practices.</p>

  <h2 class="abs section-title sub-title" style="top:763px;">Our Policy</h2>
  <div class="abs copy-head" style="top:794px;">Be Fair</div>
  <p class="abs copy" style="top:808px; width:490px;">“At Brightwell we believe that both parties benefit when pricing is fair. If margins are too low, we may sacrifice service quality, and this ultimately harms our brand. If margins are too high, our customers have an incentive to seek alternative providers, and this compromises our growth and damages client relationships.”</p>
  <div class="abs copy-head" style="top:868px;">Be Cost-Effective</div>
  <p class="abs copy" style="top:882px; width:460px;">“At Brightwell we believe that it is possible to deliver both high quality at a fair cost, by providing services that are intelligent and efficient.”</p>

  <p class="abs footer">All goods and services provided by Brightwell are provided in accordance with our Standard Terms<br>and Conditions available at <a href="#">https://www.brightwellsystems.com.au/t&amp;c</a></p>
</main>
</body>
</html>
```